Design and Renovation Company Luxury Business Card

I want to create a luxury business card for a Design and Renovation Firm . We will use our current logo. The company name is 742BUILD. We do not want anything standard. We need a very unique concept.
Please see uploaded inspiration. I really like the textured paper option. I would like the card to be thick with debossing, and/or embossing options. The logo has orange in it but I would like to see the card with and without the orange. I think the orange may make the company feel less high-end. The goal is to elevate the logo not match its vibe per se of the logo. We want something very unique, not standard at all!
I would like a space for :
Logo,
Name,
Position,
Email,
Office number,
Website Address,
Business Address,
Thank you!
Have fun!
Target Market(s)
Home owners Age 35 +
Industry/Entity Type
Design and Renovation
Contact Information for Business Card
Logo, Name, Position, Email, Office number, Website Address, Business Address,.
Colors
Designer to choose colors to be used in the design.
Requirements
Must have
- A luxury designer feel. Must be black or dark grey but open to other luxury ideas.
Nice to have
- Gold, silver, black embossing or debossing. Textured paper design.
Should not have
- A cheap look and feel.

```html
<!DOCTYPE html>
<html lang="en">
<head>
<meta charset="utf-8">
<title>742BUILD Business Card</title>
<link rel="stylesheet" href="https://fonts.googleapis.com/css2?family=Montserrat:wght@400;500&display=swap">
<style>
  :root {
    --backdrop: #a7a7a7;
    --card: #000000;
    --white: #ffffff;
    --accent: #f7941d;
    --gold: #e2b648;
    --gold-soft: #d9b04a;
  }
  * { margin: 0; padding: 0; box-sizing: border-box; }
  html, body {
    width: 1134px;
    height: 1200px;
    overflow: hidden;
    background: var(--backdrop);
    font-family: "Montserrat", sans-serif;
  }
  .canvas { position: relative; width: 1134px; height: 1200px; }
  .card {
    position: absolute;
    left: 67px;
    width: 1000px;
    height: 556px;
    background: var(--card);
  }
  .card--front { top: 30px; }
  .card--back { top: 614px; }

  /* Front */
  .front-brand {
    position: absolute;
    left: 0;
    right: 0;
    top: 0;
    bottom: 0;
    display: flex;
    align-items: center;
    justify-content: center;
    gap: 18px;
  }
  .front-dot {
    width: 18px;
    height: 18px;
    border-radius: 50%;
    background: var(--accent);
  }
  .front-name {
    color: var(--white);
    font-weight: 500;
    font-size: 52px;
    line-height: 1;
  }

  /* Back */
  .brand {
    position: absolute;
    right: 60px;
    top: 70px;
    display: flex;
    align-items: center;
    gap: 10px;
  }
  .brand-dot {
    width: 10px;
    height: 10px;
    border-radius: 50%;
    background: var(--accent);
  }
  .brand-name {
    color: var(--white);
    font-weight: 500;
    font-size: 30px;
    line-height: 1;
  }
  .details {
    position: absolute;
    left: 52px;
    top: 236px;
    color: var(--gold-soft);
  }
  .company {
    color: var(--gold);
    font-weight: 500;
    font-size: 28px;
    line-height: 1.2;
  }
  .role { font-size: 21px; margin-top: 4px; }
  .rule { height: 1px; background: var(--gold-soft); }
  .rule--short { width: 54px; margin: 14px 0 16px; }
  .rule--long { width: 390px; margin: 14px 0 16px; }
  .line { font-size: 22px; line-height: 34px; }
</style>
</head>
<body>
<main class="canvas">
  <section class="card card--front" aria-label="Card front">
    <div class="front-brand">
      <span class="front-dot"></span>
      <span class="front-name">742BUILD</span>
    </div>
  </section>

  <section class="card card--back" aria-label="Card back">
    <div class="brand">
      <span class="brand-dot"></span>
      <span class="brand-name">742BUILD</span>
    </div>
    <div class="details">
      <p class="company">742build Design And Renovation Firm</p>
      <p class="role">Ceo</p>
      <div class="rule rule--short"></div>
      <p class="line">+ 1234567890</p>
      <p class="line">Dummy City, Dummy Country</p>
      <div class="rule rule--long"></div>
      <p class="line">info@742buildstudio.com</p>
      <p class="line">www.742buildstudio.com</p>
    </div>
  </section>
</main>
</body>
</html>
```